Revamp my web site design

Willowmere Care Practitioners is a not for profit organisation focused on providing emotional support and counselling services to those with cancer or affected by cancer including those bereaved.

Our web site is intended to welcome suffers to engage with the services of its members and is also provided to encourage additional counsellors to join the organisation and then supports its members with access to materials and courses to extend their professional development.

We have a limited budget and seek to not only improve the attractiveness of the site but also improve the functionality and ease of maintenance. Especially site administrtaion should allow for uploading documents, adding new members, news and events easily.

Existing site is www.brightharbourcare.com.au

```html
<!DOCTYPE html>
<html lang="en">
<head>
<meta charset="utf-8">
<title>Willowmere Care Practitioners</title>
<link href="https://fonts.googleapis.com/css2?family=Jost:wght@400;500;600&display=swap" rel="stylesheet">
<style>
:root{
  --red:#ff1a1a;
  --ink:#2b2b2b;
  --muted:#555;
  --light:#ececec;
  --line:#cfcfcf;
  --white:#fff;
}
*{box-sizing:border-box;margin:0;padding:0}
html,body{width:675px;height:1200px;overflow:hidden;background:var(--white)}
body{position:relative;font-family:"Jost",Arial,sans-serif;color:var(--ink)}
.abs{position:absolute}

.site-header{left:0;top:0;width:675px;height:37px;background:var(--light);border-top:3px solid #222}
.brand{left:95px;top:8px;display:flex;align-items:center;gap:4px;font-size:8.5px;line-height:9px;color:var(--red);font-weight:500;width:90px}
.brand-mark{width:8px;height:8px;background:var(--red);flex:none}
.main-nav{right:94px;top:0;display:flex;height:34px}
.main-nav a{display:block;padding:0 8px;line-height:34px;font-size:7.5px;color:var(--ink);text-decoration:none;text-transform:uppercase}
.main-nav a.is-active{background:var(--red);color:var(--white)}

.hero-photo{left:62px;top:37px;width:322px;height:290px;background:linear-gradient(100deg,#e9eef2 0%,#cfd9e3 35%,#b7a69a 65%,#d9cfc8 100%)}
.hero-panel{left:384px;top:37px;width:197px;height:290px;background:var(--red);color:var(--white);padding:32px 15px 0}
.hero-title{font-size:12.5px;font-weight:500;line-height:14px;text-transform:uppercase}
.hero-text{margin-top:18px;font-size:12px;line-height:15px}
.hero-pager{position:absolute;right:75px;bottom:9px;display:flex;gap:3px;font-size:8px}
.hero-pager span{width:9px;text-align:center;line-height:10px}
.hero-pager .is-current{background:var(--white);color:var(--red)}

.service{top:340px;width:114px;height:86px;border:1px solid var(--line)}
.service-top{height:63px;background:var(--red);color:var(--white);text-align:center;font-size:5px;text-transform:uppercase;padding-top:10px}
.service-top svg{display:block;margin:0 auto 5px}
.service-more{height:22px;line-height:22px;text-align:center;font-size:5px;text-transform:uppercase;color:var(--muted)}

.section-title{left:95px;width:486px;font-size:10px;color:var(--ink);border-bottom:1px solid var(--line);padding-bottom:5px}
.section-title::after{content:"";position:absolute;left:0;bottom:-2px;width:20px;height:2px;background:var(--red)}
.slider-arrows{right:94px;top:436px;font-size:11px;color:#222;letter-spacing:6px}

.doctor{top:465px;width:155px;height:133px}
.doctor-photo{height:105px;background:linear-gradient(180deg,#f7f7f7,#dfe3e8)}
.doctor-name{position:relative;height:28px;background:var(--red);color:var(--white);font-size:8px;text-align:center;padding-top:14px;text-transform:uppercase}
.doctor-name::before{content:"";position:absolute;left:71px;top:3px;width:9px;height:9px;border-left:1px solid var(--white);border-top:1px solid var(--white);transform:rotate(45deg);transform-origin:center;top:5px}

.about{left:0;top:637px;width:675px;height:183px;background:var(--light);padding:12px 94px 0 95px;font-size:10.2px;line-height:12.3px;color:#333;text-align:justify}
.about p{margin-bottom:12.5px}

.news{top:862px;width:114px}
.news-photo{height:75px;background:linear-gradient(135deg,#dfe8ee,#a9b9c6)}
.news-title{margin-top:18px;font-size:7px;font-weight:600;line-height:9px}
.news-rule{width:22px;height:1.5px;background:var(--red);margin:4px 0 5px}
.news-text{font-size:5.6px;line-height:7px;color:#444}
.btn{display:inline-block;background:var(--red);color:var(--white);font-size:5.6px;padding:0 9px;line-height:14px}
.news .btn{margin-top:8px}

.site-footer{left:0;top:1041px;width:675px;height:125px;background:var(--light)}
.fcol{top:1056px;width:108px;font-size:5.4px;line-height:6.6px;color:#444}
.fhead{color:var(--red);font-size:6.5px;text-transform:uppercase;margin-bottom:11px}
.fbrand{display:flex;align-items:center;gap:3px;font-size:8px;line-height:8.5px;color:#555;margin-bottom:6px;width:70px}
.fbrand i{width:6px;height:6px;background:#777;flex:none}
.post{padding-bottom:4px;border-bottom:1px solid #bbb;margin-bottom:4px;position:relative}
.post::after{content:"";position:absolute;left:0;bottom:-1px;width:20px;height:1px;background:var(--red)}
.contact-line{display:flex;gap:5px;align-items:center;margin-top:4px}
.socials{display:flex;gap:5px;margin-top:8px}
.socials span{width:11px;height:11px;background:var(--red)}
.field{background:var(--white);border:1px solid #ccc;height:14px;font-size:4.5px;color:#999;padding:2px 4px}
.copyright{left:0;top:1166px;width:675px;height:34px;background:var(--red);color:var(--white);font-size:6px;padding:12px 0 0 98px}
</style>
</head>
<body>

<header class="site-header abs">
  <div class="brand abs"><span class="brand-mark"></span>Willowmere Care Practitioners</div>
  <nav class="main-nav abs">
    <a class="is-active" href="#">Home</a><a href="#">Contact us</a><a href="#">News</a><a href="#">Events</a><a href="#">Articles</a><a href="#">Find a counsellor</a><a href="#">Members</a>
  </nav>
</header>

<div class="hero-photo abs" role="img" aria-label="Smiling doctor holding a blue folder with a family in the background"></div>
<section class="hero-panel abs">
  <h1 class="hero-title">Aenean euismod nibh ligula, eget ultrices nibh pulvinar quis</h1>
  <p class="hero-text">Aenean euismod nibh ligula, Eget ultrices nibh pulvinar Curabitur et ultrices lorem. Duis fringillamauris eu dapi Euismod, quam massa.</p>
  <div class="hero-pager"><span>1</span><span>2</span><span class="is-current">3</span><span>4</span><span>5</span></div>
</section>

<div class="service abs" style="left:95px">
  <div class="service-top">
    <svg width="44" height="30" viewBox="0 0 44 30" fill="none" stroke="#fff" stroke-width="2.5"><rect x="4" y="6" width="36" height="6" rx="3"/><path d="M12 12l18 12M32 12L14 24"/><circle cx="12" cy="26" r="2.5"/><circle cx="32" cy="26" r="2.5"/></svg>
    Aenean euismod</div>
  <div class="service-more">Learn more</div>
</div>
<div class="service abs" style="left:218px">
  <div class="service-top">
    <svg width="30" height="30" viewBox="0 0 30 30" fill="none" stroke="#fff" stroke-width="2.2"><rect x="5" y="4" width="20" height="25" rx="2"/><rect x="11" y="1.5" width="8" height="5" fill="#fff"/><path d="M8 18h4l2-5 3 9 2-4h3"/></svg>
    Du fring imauris</div>
  <div class="service-more">Learn more</div>
</div>
<div class="service abs" style="left:341px">
  <div class="service-top">
    <svg width="30" height="30" viewBox="0 0 30 30" fill="#fff"><path d="M15 27C5 19 3 15 3 10a6 6 0 0 1 12-2 6 6 0 0 1 12 2c0 5-2 9-12 17z"/></svg>
    Viverra aliquam</div>
  <div class="service-more">Learn more</div>
</div>
<div class="service abs" style="left:467px">
  <div class="service-top">
    <svg width="30" height="30" viewBox="0 0 30 30" fill="none" stroke="#fff" stroke-width="2.2"><rect x="8" y="3" width="14" height="20" rx="4"/><path d="M11 10h4M11 14h4M15 23v6"/></svg>
    Aenean euismod</div>
  <div class="service-more">Learn more</div>
</div>

<h2 class="section-title abs" style="top:435px">Our Doctors</h2>
<div class="slider-arrows abs">&lsaquo;&rsaquo;</div>

<div class="doctor abs" style="left:95px"><div class="doctor-photo" role="img" aria-label="Two doctors in white coats"></div><div class="doctor-name">Pell Entesque</div></div>
<div class="doctor abs" style="left:260px"><div class="doctor-photo" role="img" aria-label="Two doctors, one wearing a surgical mask"></div><div class="doctor-name">Tom Hadley</div></div>
<div class="doctor abs" style="left:426px"><div class="doctor-photo" role="img" aria-label="Doctor with a family group"></div><div class="doctor-name">Anderala Roz</div></div>

<h2 class="section-title abs" style="top:617px">Willowmere Care Practitioners&nbsp; Inc</h2>

<section class="about abs">
  <p>A diagnosis of cancer is a devastating experience for most people.</p>
  <p>Many people can get support by talking to close family or friends. However, it can sometimes help to talk to someone from outside of that circle who has been trained to listen and help you explore your feelings.&nbsp; You may feel as if you are riding an emotional rollercoaster. Often talking of your distress to those close to you can be difficult and painful.</p>
  <p>When someone is diagnosed with cancer, they and their family can feel shocked, numb, directionless and afraid. They often feel they need to talk things through in confidence with someone who understands the emotional challenges of cancer.</p>
  <p>&nbsp;Talking to a counsellor or psychologist experienced in cancer issues can ease the sense of isolation you may feel and help you find ways to face the challenges ahead.</p>
</section>

<h2 class="section-title abs" style="top:829px">Latest News</h2>

<article class="news abs" style="left:95px"><div class="news-photo" role="img" aria-label="Two smiling doctors"></div><h3 class="news-title">Vestibulum hendrerit vestibulum lacus quis imperdieted.</h3><div class="news-rule"></div><p class="news-text">Aenean euismod nibh ligula, eget ultrices nibh pulvinar quis. Curabitur et ultrices lorem. Duis fringilla, mauris eu</p><a class="btn">Read more</a></article>
<article class="news abs" style="left:219px"><div class="news-photo" role="img" aria-label="Scientist working in a laboratory"></div><h3 class="news-title">Vestibulum hendrerit vestibulum lacus quis imperdieted.</h3><div class="news-rule"></div><p class="news-text">Aenean euismod nibh ligula, eget ultrices nibh pulvinar quis. Curabitur et ultrices lorem. Duis fringilla, mauris eu</p><a class="btn">Read more</a></article>
<article class="news abs" style="left:343px"><div class="news-photo" role="img" aria-label="Doctor examining a young child"></div><h3 class="news-title">Vestibulum hendrerit vestibulum lacus quis imperdieted.</h3><div class="news-rule"></div><p class="news-text">Aenean euismod nibh ligula, eget ultrices nibh pulvinar quis. Curabitur et ultrices lorem. Duis fringilla, mauris eu</p><a class="btn">Read more</a></article>
<article class="news abs" style="left:467px"><div class="news-photo" role="img" aria-label="Doctor talking with an elderly patient"></div><h3 class="news-title">Vestibulum hendrerit vestibulum lacus quis imperdieted.</h3><div class="news-rule"></div><p class="news-text">Aenean euismod nibh ligula, eget ultrices nibh pulvinar quis. Curabitur et ultrices lorem. Duis fringilla, mauris eu</p><a class="btn">Read more</a></article>

<footer class="site-footer abs"></footer>

<div class="fcol abs" style="left:95px">
  <h4 class="fhead">About us</h4>
  <div class="fbrand"><i></i>Willowmere Care Practitioners</div>
  <p>A diagnosis of cancer is a devastating experience for most people.</p>
  <a class="btn" style="margin-top:11px">Read more</a>
</div>
<div class="fcol abs" style="left:218px;width:104px">
  <h4 class="fhead">Latest posts</h4>
  <p class="post">consectetur adipiscing elit. Suspend-isse hendrerit accumsan turpis</p>
  <p class="post">consectetur adipiscing elit. Suspend-isse hendrerit accumsan turpis</p>
  <p class="post">consectetur adipiscing elit. Suspend-isse hendrerit accumsan turpis</p>
</div>
<div class="fcol abs" style="left:343px">
  <h4 class="fhead">Contact info</h4>
  <p>Sectetur adipiscing elitisse hendrerit accumsan turpis adipiscing elitisse.</p>
  <div class="contact-line"><svg width="7" height="6" viewBox="0 0 7 6" fill="#f11"><path d="M3.5 0L7 3H6v3H1V3H0z"/></svg>Suspendisse hendrerit accumsan</div>
  <div class="contact-line"><svg width="7" height="6" viewBox="0 0 7 6" fill="#f11"><path d="M0 1.5Q3.5-1 7 1.5v1H5V2H2v.5H0zM1 3h5v3H1z"/></svg>+61 3 9555 0142</div>
  <div class="contact-line"><svg width="7" height="6" viewBox="0 0 7 6" fill="none" stroke="#f11" stroke-width=".8"><rect x=".5" y=".5" width="6" height="5"/><path d="M.5 .5l3 2.5 3-2.5"/></svg>hello@willowmerecare.org</div>
  <div class="socials"><span></span><span></span><span></span></div>
</div>
<div class="fcol abs" style="left:465px;width:116px">
  <h4 class="fhead">Quick contact</h4>
  <div style="display:flex;gap:3px;margin-top:-4px"><div class="field" style="width:56px">Name</div><div class="field" style="width:56px">Email</div></div>
  <div class="field" style="height:34px;margin-top:4px">Message</div>
  <div style="text-align:right;margin-top:7px"><a class="btn">Send</a></div>
</div>

<div class="copyright abs">&copy; Willowmere Care Practitioners Inc</div>

</body>
</html>
```